Design a Mobile App for Landscape Businesses

This project is to design the first three screens for a mobile app for Landscape and Lawncare businesses. This app will serve as a directory for homeowners to locate landscape and lawn care businesses and for landscape businesses and contractors to run their business. See the attached PDF for more information and example
Here is the link to the description https://brevlinq.test/k3r92P

Target Market(s)

Landscape and lawn care business, gardeners, home owners

Industry/Entity Type

Landscape Gardening

Logo Text

Quillmoray

Colors

Designer to choose colors to be used in the design.

```html
<!DOCTYPE html>
<html lang="en">
<head>
<meta charset="utf-8">
<title>Lawncare businesses</title>
<link rel="stylesheet" href="https://fonts.googleapis.com/css2?family=Arimo:wght@400;500;600&display=swap">
<style>
:root{
  --green-top:#3f8a3a;
  --green-bottom:#2f6a2c;
  --green-button:#43853a;
  --white:#ffffff;
  --ink:#1f1f1f;
  --body:#333333;
  --divider:#e3e3e3;
}
*{margin:0;padding:0;box-sizing:border-box}
html,body{width:675px;height:1200px;overflow:hidden;background:var(--white)}
body{font-family:"Arimo",Helvetica,Arial,sans-serif;color:var(--ink);position:relative}
.app-header{position:absolute;left:0;top:0;width:675px;height:124px;background:linear-gradient(var(--green-top),var(--green-bottom));color:var(--white)}
.status-bar{position:absolute;left:14px;right:12px;top:14px;height:28px;display:flex;justify-content:space-between;align-items:center;font-size:20px;font-weight:500}
.status-left,.status-right{display:flex;align-items:center;gap:8px}
.screen-title{position:absolute;left:0;right:0;top:66px;text-align:center;font-size:26px;font-weight:500;letter-spacing:.2px}
.header-icon{position:absolute;top:68px}
.menu-icon{left:18px}
.settings-icon{right:16px}
.listing{position:absolute;left:36px;width:610px;height:190px}
.listing-photo{position:absolute;left:0;top:0;width:210px;height:190px;border-radius:26px;box-shadow:0 5px 9px rgba(0,0,0,.35)}
.photo-grass{background:linear-gradient(150deg,#c6d98a,#8fb13a 55%,#6e9a2a)}
.photo-garden{background:radial-gradient(circle at 70% 25%,#c9f07a,#4aa82c 45%,#1f6a1a)}
.photo-building{background:linear-gradient(#f3e3b8 0,#ecd5a0 65%,#86ac50 85%,#6f9a3e)}
.listing-info{position:absolute;left:246px;top:14px;width:380px}
.listing-name{font-size:21px;font-weight:500;letter-spacing:.3px}
.rating{font-size:17px;letter-spacing:-1px;margin-top:4px;color:#000}
.listing-desc{font-size:13.5px;line-height:24px;color:var(--body);margin-top:3px}
.listing-phone{font-size:17px;margin-top:10px;color:var(--ink)}
.divider{position:absolute;left:50px;width:587px;height:4px;background:var(--divider);border-radius:2px}
.quote-button{position:absolute;left:52px;top:966px;width:577px;height:74px;background:var(--green-button);color:var(--white);border-radius:4px;display:flex;align-items:center;justify-content:center;font-size:22px;font-weight:500;letter-spacing:.5px}
.tab-bar{position:absolute;left:0;top:1085px;width:675px;height:115px;background:linear-gradient(var(--green-top),var(--green-bottom))}
.tab-icon{position:absolute;top:38px}
.tab-center{position:absolute;left:286px;top:9px;width:100px;height:100px;border-radius:50%;background:#4e9145;border:2px solid var(--white);box-shadow:0 4px 8px rgba(0,0,0,.4);display:flex;align-items:center;justify-content:center}
</style>
</head>
<body>
<header class="app-header">
  <div class="status-bar">
    <div class="status-left">
      <svg width="58" height="12" viewBox="0 0 58 12" fill="#fff"><circle cx="6" cy="6" r="5"/><circle cx="17" cy="6" r="5"/><circle cx="28" cy="6" r="5"/><circle cx="39" cy="6" r="5"/><circle cx="50" cy="6" r="4.3" fill="none" stroke="#fff" stroke-width="1.4"/></svg>
      <span>Carrier</span>
      <svg width="20" height="14" viewBox="0 0 20 14" fill="none" stroke="#fff" stroke-width="2"><path d="M2 5a12 12 0 0 1 16 0M5 8.5a7 7 0 0 1 10 0"/><circle cx="10" cy="12" r="1.5" fill="#fff" stroke="none"/></svg>
    </div>
    <div class="status-right">
      <svg width="22" height="22" viewBox="0 0 22 22" fill="none" stroke="#fff" stroke-width="1.8"><path d="M19 11a8 8 0 1 1-3-6.2"/><rect x="8" y="10" width="6" height="5" fill="#fff" stroke="none"/><path d="M9 10V8.5a2 2 0 0 1 4 0V10"/></svg>
      <span>100%</span>
      <svg width="44" height="20" viewBox="0 0 44 20"><rect x="1" y="1" width="38" height="18" rx="4" fill="none" stroke="#fff" stroke-width="1.6"/><rect x="3.5" y="3.5" width="33" height="13" rx="2" fill="#fff"/><rect x="40.5" y="7" width="2.5" height="6" rx="1" fill="#fff"/></svg>
    </div>
  </div>
  <svg class="header-icon menu-icon" width="32" height="24" viewBox="0 0 32 24" fill="#fff"><rect x="0" y="1" width="4" height="4"/><rect x="8" y="1.5" width="24" height="3"/><rect x="0" y="10" width="4" height="4"/><rect x="8" y="10.5" width="24" height="3"/><rect x="0" y="19" width="4" height="4"/><rect x="8" y="19.5" width="24" height="3"/></svg>
  <h1 class="screen-title">Lawncare businesses</h1>
  <svg class="header-icon settings-icon" width="26" height="26" viewBox="0 0 26 26" fill="none" stroke="#fff" stroke-width="1.8"><path d="M11 2h4l.7 3 2.4 1.4 2.9-1 2 3.4-2.3 2.1v2.2l2.3 2.1-2 3.4-2.9-1-2.4 1.4-.7 3h-4l-.7-3-2.4-1.4-2.9 1-2-3.4 2.3-2.1v-2.2L2.7 8.8l2-3.4 2.9 1L10 5z"/><circle cx="13" cy="13" r="3.6"/></svg>
</header>

<main>
  <article class="listing" style="top:190px">
    <div class="listing-photo photo-grass" role="img" aria-label="Bare feet resting on fresh green grass"></div>
    <div class="listing-info">
      <h2 class="listing-name">Lawncare businesses</h2>
      <div class="rating">★★★★★</div>
      <p class="listing-desc">Lorem Ipsum is simply dummy text of the printing and typesetting industry. Lorem Ipsum has been the indus-try's</p>
      <p class="listing-phone">(123) 456 6789</p>
    </div>
  </article>
  <div class="divider" style="top:417px"></div>

  <article class="listing" style="top:454px">
    <div class="listing-photo photo-garden" role="img" aria-label="Sunlit green garden with trees and tall grass"></div>
    <div class="listing-info">
      <h2 class="listing-name">Lawncare businesses</h2>
      <div class="rating">★★★★★</div>
      <p class="listing-desc">Lorem Ipsum is simply dummy text of the printing and typesetting industry. Lorem Ipsum has been the indus-try's</p>
      <p class="listing-phone">(123) 456 6789</p>
    </div>
  </article>
  <div class="divider" style="top:684px"></div>

  <article class="listing" style="top:723px">
    <div class="listing-photo photo-building" role="img" aria-label="Group of residents on a lawn in front of a cream apartment building"></div>
    <div class="listing-info">
      <h2 class="listing-name">Lawncare businesses</h2>
      <div class="rating">★★★★★</div>
      <p class="listing-desc">Lorem Ipsum is simply dummy text of the printing and typesetting industry. Lorem Ipsum has been the indus-try's</p>
      <p class="listing-phone">(123) 456 6789</p>
    </div>
  </article>

  <div class="quote-button">REQUEST A QUOTE</div>
</main>

<nav class="tab-bar">
  <svg class="tab-icon" style="left:60px" width="38" height="30" viewBox="0 0 38 30" fill="#fff"><rect y="2" width="38" height="3"/><rect y="13.5" width="38" height="3"/><rect y="25" width="38" height="3"/></svg>
  <svg class="tab-icon" style="left:182px;top:36px" width="40" height="36" viewBox="0 0 40 36" fill="none" stroke="#fff" stroke-width="1.8"><path d="M4 34v-4c0-4 4-6 8-7.5-3-2-4-5-4-9a7 7 0 0 1 14 0c0 4-1 7-4 9 4 1.5 8 3.5 8 7.5v4z"/><path d="M22 7a7 7 0 0 1 10 6c0 4-1 7-4 9 4 1.5 8 3.5 8 7.5V34h-8"/></svg>
  <div class="tab-center">
    <svg width="40" height="54" viewBox="0 0 40 54" fill="none" stroke="#fff" stroke-width="2"><path d="M20 52C10 36 3 27 3 19a17 17 0 0 1 34 0c0 8-7 17-17 33z"/><circle cx="20" cy="19" r="6"/></svg>
  </div>
  <svg class="tab-icon" style="left:465px;top:35px" width="34" height="38" viewBox="0 0 34 38" fill="none" stroke="#fff" stroke-width="1.6"><rect x="1" y="5" width="32" height="32" rx="2"/><path d="M1 12h32M8 1v7M26 1v7M6 17h22v15H6zM6 22h22M6 27h22M11.5 17v15M17 17v15M22.5 17v15"/></svg>
  <svg class="tab-icon" style="left:578px;top:36px" width="38" height="38" viewBox="0 0 38 38" fill="none" stroke="#fff" stroke-width="2.2"><circle cx="16" cy="16" r="13"/><path d="M25.5 25.5L36 36"/></svg>
</nav>
</body>
</html>
```